Family Farm Looking for meat label

We have a small farm in Italy with two types of cow "Piemontese" and "Pezzata Rossa Valdostana". We need label ( about 5x5 cm) to put on the boxes and on every single piece of meat.

Target Market(s)

private client

Industry/Entity Type

family farm

Colors

Designer to choose colors to be used in the design.

Requirements
Must have
• to write "Azienda Agricola Il Mulinetto" and the cow like our cow not differently. the Piemontese breed cow has the typical physical shapes as in the photo. No photo on the label just a drawing o something like that.
Nice to have
• just a one label, clear, fine and clean . Maybe with pastel color or watercolor. We are a small family farm.
Should not have
• no photo, no another type of cow

```html
<!DOCTYPE html>
<html lang="en">
<head>
<meta charset="utf-8">
<title>Il Mulinetto – Piemontese Beef Label</title>
<link rel="stylesheet" href="https://fonts.googleapis.com/css2?family=Oswald:wght@300;400;600&family=Archivo:wght@800;900&display=swap">
<style>
  :root {
    --backdrop: #e6e7e8;
    --farm-green: #34b457;
    --flag-red: #c8262b;
    --cream: #f4f2e8;
    --ink: #1e1e1e;
    --white: #ffffff;
  }
  * { margin: 0; padding: 0; box-sizing: border-box; }
  html, body { width: 1200px; height: 1200px; overflow: hidden; background: var(--backdrop); }
  .canvas { position: relative; width: 1200px; height: 1200px; }

  .label {
    position: absolute; left: 287px; top: 286px; width: 594px; height: 594px;
    background: var(--white);
    border: 3px solid var(--farm-green);
    border-radius: 30px;
    box-shadow: 14px 14px 22px rgba(0,0,0,0.12);
  }
  .label-panel {
    position: absolute; left: 8px; top: 9px; width: 569px; height: 553px;
    background: var(--cream);
    border: 4px solid var(--flag-red);
    border-radius: 20px;
  }
  .brand-banner { position: absolute; left: 91px; top: -3px; width: 404px; height: 216px; }
  .brand-name {
    position: absolute; left: 100px; top: 112px; width: 300px; text-align: center;
    font-family: "Oswald", sans-serif; font-weight: 600; font-size: 50px;
    color: var(--white); letter-spacing: 0.01em; line-height: 1;
  }
  .brand-dot {
    position: absolute; left: 240px; top: 55px; width: 18px; height: 18px;
    border: 2px solid var(--white); border-radius: 50%;
  }
  .product-name {
    position: absolute; left: 0; top: 228px; width: 588px; text-align: center;
    font-family: "Oswald", sans-serif; font-weight: 600; font-size: 84px; line-height: 1;
    color: var(--farm-green); letter-spacing: 0.005em;
  }
  .breed-illustration {
    position: absolute; left: 207px; top: 352px; width: 171px; height: 143px;
    border-radius: 40% 45% 20% 20%;
    background: radial-gradient(ellipse at 50% 50%, #c9cbbf 0%, #a9ac9e 55%, rgba(169,172,158,0) 78%);
    z-index: 1;
  }
  .product-kind {
    position: absolute; left: -10px; top: 317px; width: 588px; text-align: center;
    font-family: "Archivo", sans-serif; font-weight: 900; font-size: 40px; line-height: 1;
    color: var(--farm-green); letter-spacing: 0.38em; padding-left: 0.38em;
    z-index: 2;
  }
  .claims { position: absolute; font-family: "Oswald", sans-serif; font-weight: 400; color: var(--ink); text-align: center; line-height: 0.98; font-size: 22px; }
  .claims-left { left: 3px; top: 446px; width: 180px; }
  .claims-left p + p { margin-top: 8px; }
  .claims-right { left: 388px; top: 458px; width: 180px; }
  .claims-right p + p { margin-top: 8px; }
  .divider { position: absolute; top: 455px; width: 3px; height: 90px; background: var(--farm-green); }
  .divider-left { left: 176px; }
  .divider-right { left: 406px; }
  .feed-claim {
    position: absolute; left: 180px; top: 503px; width: 227px; text-align: center;
    font-family: "Archivo", sans-serif; font-weight: 800; font-size: 29px; line-height: 1;
    color: var(--farm-green);
  }
  .farm-name {
    position: absolute; left: 0; top: 561px; width: 588px; text-align: center;
    font-family: "Archivo", sans-serif; font-weight: 800; font-size: 21px; line-height: 1;
    color: var(--farm-green); letter-spacing: 0.14em;
  }
</style>
</head>
<body>
<div class="canvas">
  <div class="label">
    <div class="label-panel"></div>

    <svg class="brand-banner" viewBox="0 0 404 216" aria-hidden="true">
      <polygon points="0,0 404,0 404,213 202,188 0,213" fill="var(--farm-green)"/>
    </svg>
    <span class="brand-dot"></span>
    <div class="brand-name">IL MULINETTO</div>

    <h1 class="product-name">PIEMONTESE</h1>
    <div class="breed-illustration" role="img" aria-label="Engraved-style drawing of a Piemontese bull standing on grass"></div>
    <div class="product-kind">BEEF</div>

    <div class="claims claims-left">
      <p>NO ADDED<br>HORMONES</p>
      <p>NO ANIMAL BY<br>PRODUCTS</p>
    </div>
    <span class="divider divider-left"></span>
    <div class="feed-claim">GRASS FED</div>
    <span class="divider divider-right"></span>
    <div class="claims claims-right">
      <p>ANTIBIOTIC<br>FREE</p>
      <p>250G</p>
    </div>

    <div class="farm-name">AZIENDA AGRICOLA IL MULINETTO</div>
  </div>
</div>
</body>
</html>
```